Online video and marketing company business cards

Need to get some new business cards designed to fit with our new logo. The cards should be professional, clean and simple.

Cards should have:

Name
Position
2 line address
telephone
mobile
email address
web address

We need to have our logo and if possible say what we do...
ONLINE FILM PRODUCTION & STRATEGY

Marketing

```html
<!DOCTYPE html>
<html lang="en">
<head>
<meta charset="utf-8">
<title>Brightlane business cards</title>
<link href="https://fonts.googleapis.com/css2?family=Mulish:wght@400;700;800&display=swap" rel="stylesheet">
<style>
  :root {
    --backdrop: #e4e4e6;
    --card-white: #f3f3f4;
    --navy: #1f4466;
    --teal: #3f93ad;
    --teal-light: #7fc0d6;
    --blue-top: #2e6f8e;
    --blue-bottom: #223f61;
    --grey-text: #5d6e7f;
    --rule: #c7ccd2;
  }
  * { margin: 0; padding: 0; box-sizing: border-box; }
  html, body { width: 1200px; height: 931px; overflow: hidden; }
  body {
    background: var(--backdrop);
    font-family: "Mulish", "Helvetica Neue", Arial, sans-serif;
    position: relative;
  }
  .card {
    position: absolute;
    width: 540px;
    height: 310px;
    border-radius: 26px;
    box-shadow: 0 10px 24px rgba(0,0,0,0.18);
  }
  .card-front {
    left: 70px; top: 130px;
    background: var(--card-white);
  }
  .card-back {
    left: 590px; top: 490px;
    background: linear-gradient(160deg, var(--blue-top), var(--blue-bottom));
  }
  .brand {
    position: absolute;
    display: flex;
    align-items: center;
    gap: 10px;
  }
  .brand-dot {
    width: 22px; height: 22px;
    border-radius: 50%;
  }
  .brand-name {
    font-weight: 800;
    letter-spacing: -0.5px;
    line-height: 1;
  }
  .card-front .brand { left: 175px; top: 44px; }
  .card-front .brand-dot { background: var(--teal); }
  .card-front .brand-name { font-size: 40px; color: var(--teal); }

  .holder { position: absolute; left: 40px; top: 150px; }
  .holder-name {
    font-weight: 800; font-size: 17px; letter-spacing: 1px;
    color: var(--navy); text-transform: uppercase;
  }
  .holder-role { font-size: 14px; color: var(--grey-text); }

  .contacts {
    position: absolute; left: 40px; right: 30px; bottom: 36px;
    display: flex; align-items: flex-end;
    font-size: 13px; color: var(--grey-text); line-height: 1.55;
  }
  .contact-group { padding: 0 18px; border-left: 1px solid var(--rule); }
  .contact-group:first-child { padding-left: 0; border-left: none; }
  .contact-line { display: flex; align-items: center; gap: 7px; white-space: nowrap; }
  .contact-line svg { width: 13px; height: 13px; flex: none; }

  .card-back .brand { left: 120px; top: 118px; }
  .card-back .brand-dot { background: #ffffff; }
  .card-back .brand-name { font-size: 46px; color: var(--teal-light); }
  .tagline {
    position: absolute; right: 40px; top: 196px;
    text-align: right; color: #d6e6ef;
    font-size: 17px; line-height: 1.3; letter-spacing: 0.3px;
  }
</style>
</head>
<body>

<section class="card card-front" aria-label="Business card front">
  <div class="brand">
    <span class="brand-dot"></span>
    <span class="brand-name">brightlane</span>
  </div>

  <div class="holder">
    <p class="holder-name">Sam Porter</p>
    <p class="holder-role">Manager</p>
  </div>

  <div class="contacts">
    <div class="contact-group">
      <p class="contact-line">
        <svg viewBox="0 0 14 14"><rect x="1" y="1" width="12" height="12" rx="3" fill="none" stroke="var(--teal)" stroke-width="1.4"/><rect x="4.5" y="3.5" width="5" height="7" rx="1" fill="var(--teal)"/></svg>
        +44(0)207 555 0148
      </p>
      <p class="contact-line">
        <svg viewBox="0 0 14 14"><circle cx="7" cy="7" r="6" fill="none" stroke="var(--teal)" stroke-width="1.4"/><path d="M4.5 4 L6 4 L6.5 5.5 L5.7 6.3 Q6.6 7.6 7.7 8.3 L8.5 7.5 L10 8 L10 9.5 Q6 10 4.5 4 Z" fill="var(--teal)"/></svg>
        +44(0)203 555 0172
      </p>
    </div>
    <div class="contact-group">
      <p class="contact-line">
        <svg viewBox="0 0 14 14"><circle cx="7" cy="7" r="6" fill="none" stroke="var(--teal)" stroke-width="1.4"/><rect x="3.8" y="4.8" width="6.4" height="4.4" fill="none" stroke="var(--teal)" stroke-width="1"/><path d="M3.8 4.8 L7 7.3 L10.2 4.8" fill="none" stroke="var(--teal)" stroke-width="1"/></svg>
        info@brightlane.tv
      </p>
      <p class="contact-line">
        <svg viewBox="0 0 14 14"><circle cx="7" cy="7" r="6" fill="none" stroke="var(--teal)" stroke-width="1.4"/><ellipse cx="7" cy="7" rx="2.6" ry="6" fill="none" stroke="var(--teal)" stroke-width="1"/><line x1="1" y1="7" x2="13" y2="7" stroke="var(--teal)" stroke-width="1"/></svg>
        www.brightlane.tv
      </p>
    </div>
    <div class="contact-group">
      <p>12 Harlow Mews</p>
      <p>London E2 4RT U.K.</p>
    </div>
  </div>
</section>

<section class="card card-back" aria-label="Business card back">
  <div class="brand">
    <span class="brand-dot"></span>
    <span class="brand-name">brightlane</span>
  </div>
  <p class="tagline">Online Film Production<br>&amp; Strategy</p>
</section>

</body>
</html>
```